Copper Lantern General Contracting Business Card

My company is a General Contracting and Handyman service based in a private community in Northeast Pennsylvania.
Our cliental is a mix of year round and seasonal homeowners
We pride ourselves i using new and innovative building techniques and always try to build with pride and integrity
Please check my website f(under construction) or a list of services and more information
The files below are my logo and my facebook business page profile pic

Industry/Entity Type

Building

Contact Information for Business Card

Copper Lantern General Contracting
Dale Hurst
Birch Ridge, Pennsylvania
570-555-0147
dale@cprlantern.com
www.cprlantern.com
www.neighborpage.net/copperlanterncontracting

```html
<!DOCTYPE html>
<html lang="en">
<head>
<meta charset="utf-8">
<title>Copper Lantern General Contracting – Business Card</title>
<link rel="stylesheet" href="https://fonts.googleapis.com/css2?family=Open+Sans:wght@400;700;800&display=swap">
<style>
  :root {
    --stage: #2b2b2b;
    --brand-red: #cc2f2f;
    --paper: #f7f7f7;
    --ink: #1e1e1e;
    --white: #ffffff;
  }
  html, body {
    margin: 0;
    padding: 0;
    width: 1200px;
    height: 790px;
    overflow: hidden;
    background: var(--stage);
    font-family: "Open Sans", Arial, sans-serif;
  }
  .stage {
    position: relative;
    width: 1200px;
    height: 790px;
  }
  .card {
    position: absolute;
    top: 252px;
    width: 500px;
    height: 286px;
    overflow: hidden;
    box-shadow: 0 10px 28px rgba(0,0,0,.45);
  }
  .card--front {
    left: 70px;
    background: var(--brand-red);
    display: flex;
    align-items: center;
    justify-content: center;
  }
  .front-mark {
    display: flex;
    align-items: center;
    gap: 16px;
    color: var(--white);
    font-weight: 800;
  }
  .front-mark__square {
    width: 58px;
    height: 58px;
    background: var(--white);
  }
  .front-mark__name {
    line-height: 1.05;
    text-transform: uppercase;
  }
  .front-mark__line1 { display: block; font-size: 30px; letter-spacing: .5px; }
  .front-mark__line2 { display: block; font-size: 15px; letter-spacing: 3px; }

  .card--back {
    left: 630px;
    background: var(--brand-red);
  }
  .back-rules {
    position: absolute;
    inset: 0;
  }
  .back-logo {
    position: absolute;
    left: 22px;
    top: 40px;
    display: flex;
    align-items: center;
    gap: 9px;
    color: var(--ink);
    font-weight: 800;
    text-transform: uppercase;
    line-height: 1.05;
  }
  .back-logo__square {
    width: 30px;
    height: 30px;
    background: var(--brand-red);
  }
  .back-logo__line1 { display: block; font-size: 17px; }
  .back-logo__line2 { display: block; font-size: 8.5px; letter-spacing: 2px; }
  .holder-name {
    position: absolute;
    right: 30px;
    top: 30px;
    margin: 0;
    font-size: 19px;
    font-weight: 700;
    color: var(--ink);
  }
  .contact-list {
    position: absolute;
    left: 22px;
    bottom: 16px;
    margin: 0;
    padding: 0;
    list-style: none;
    color: var(--white);
    font-size: 12px;
    line-height: 19px;
  }
  .contact-list li {
    display: flex;
    align-items: center;
    gap: 7px;
  }
  .contact-icon {
    width: 12px;
    height: 12px;
    flex: none;
  }
</style>
</head>
<body>
<main class="stage">

  <section class="card card--front" aria-label="Card front">
    <div class="front-mark">
      <span class="front-mark__square"></span>
      <span class="front-mark__name">
        <span class="front-mark__line1">Copper Lantern</span>
        <span class="front-mark__line2">General Contracting</span>
      </span>
    </div>
  </section>

  <section class="card card--back" aria-label="Card back">
    <svg class="back-rules" width="500" height="286" viewBox="0 0 500 286" aria-hidden="true">
      <rect x="0" y="0" width="500" height="122" fill="var(--paper)"/>
      <polygon points="0,122 500,122 500,141 0,141" fill="var(--paper)"/>
      <polygon points="0,124 385,124 398,112 411,124 500,124 500,131 0,131" fill="var(--brand-red)"/>
    </svg>

    <div class="back-logo">
      <span class="back-logo__square"></span>
      <span>
        <span class="back-logo__line1">Copper Lantern</span>
        <span class="back-logo__line2">General Contracting</span>
      </span>
    </div>

    <h1 class="holder-name">Dale Hurst</h1>

    <ul class="contact-list">
      <li>
        <svg class="contact-icon" viewBox="0 0 12 12" aria-hidden="true"><circle cx="6" cy="6" r="6" fill="#fff"/><path d="M4 3h1.4l.6 1.6-.8.6a4 4 0 0 0 1.6 1.6l.6-.8 1.6.6V8.6A.6.6 0 0 1 8 9 5 5 0 0 1 3 4a.6.6 0 0 1 .4-.6z" fill="var(--brand-red)"/></svg>
        570-555-0147
      </li>
      <li>
        <svg class="contact-icon" viewBox="0 0 12 12" aria-hidden="true"><circle cx="6" cy="6" r="6" fill="#fff"/><rect x="3" y="4" width="6" height="4.2" fill="none" stroke="var(--brand-red)" stroke-width=".9"/><path d="M3 4l3 2.4L9 4" fill="none" stroke="var(--brand-red)" stroke-width=".9"/></svg>
        dale@cprlantern.com
      </li>
      <li>
        <svg class="contact-icon" viewBox="0 0 12 12" aria-hidden="true"><circle cx="6" cy="6" r="6" fill="#fff"/><circle cx="6" cy="6" r="3.2" fill="none" stroke="var(--brand-red)" stroke-width=".8"/><path d="M2.8 6h6.4M6 2.8v6.4" stroke="var(--brand-red)" stroke-width=".8"/></svg>
        www.cprlantern.com
      </li>
      <li>
        <svg class="contact-icon" viewBox="0 0 12 12" aria-hidden="true"><circle cx="6" cy="6" r="6" fill="#fff"/></svg>
        www.neighborpage.net/copperlanterncontracting
      </li>
      <li>
        <svg class="contact-icon" viewBox="0 0 12 12" aria-hidden="true"><circle cx="6" cy="6" r="6" fill="#fff"/><path d="M6 2.6a2.3 2.3 0 0 1 2.3 2.3C8.3 6.6 6 9.4 6 9.4S3.7 6.6 3.7 4.9A2.3 2.3 0 0 1 6 2.6z" fill="var(--brand-red)"/><circle cx="6" cy="4.9" r=".8" fill="#fff"/></svg>
        Birch Ridge, Pennsylvania
      </li>
    </ul>
  </section>

</main>
</body>
</html>
```